We need a letterhead incorporating our logo (uploaded file), with the name of our organization (Dunmore Hollis County Police Association) and our slogan (Strength in Unity). Dark blue should be incorporated somewhere in the design, either the font color or elsewhere. Please make sure our logo is included in the design. The organization is a law enforcement union type group.

Target Market(s)

Members of our association, policticians, and anyone receiving our letters

Colors
0255a3

Requirements
Must have
• Our logo, Association name, and slogan.
Nice to have
• A professional and eye-catching letterhead design incorporating the logo, name, and slogan.

```html
<!DOCTYPE html>
<html lang="en">
<head>
<meta charset="utf-8">
<title>Dunmore Hollis County Police Association – Letterhead</title>
<link href="https://fonts.googleapis.com/css2?family=Open+Sans:wght@400;600&family=Roboto:wght@400&display=swap" rel="stylesheet">
<style>
  :root {
    --backdrop: #e9e9ea;
    --paper: #fbfbfb;
    --ink: #5a5a5a;
    --ink-dark: #3c3c3c;
    --brand-blue: #0255a3;
    --icon-blue: #4d7fc4;
    --signature-tone: #cfcfcf;
  }
  * { box-sizing: border-box; margin: 0; padding: 0; }
  html, body {
    width: 1200px; height: 795px; overflow: hidden;
    background: var(--backdrop);
  }
  .canvas {
    width: 1200px; height: 795px;
    display: flex; align-items: center; justify-content: center;
  }
  .letterhead {
    position: relative;
    width: 536px; height: 757px;
    background: var(--paper);
    box-shadow: 0 2px 10px rgba(0,0,0,0.12);
    font-family: "Open Sans", sans-serif;
    color: var(--ink);
  }
  .brand {
    position: absolute; top: 44px; left: 52px;
    display: flex; align-items: center; gap: 10px;
  }
  .brand-mark {
    width: 34px; height: 34px; border-radius: 50%;
    background: var(--brand-blue);
  }
  .brand-name {
    font-family: "Open Sans", sans-serif;
    font-weight: 600; font-size: 12px; line-height: 1.3;
    color: var(--brand-blue);
    width: 160px;
  }
  .letter-body {
    position: absolute; top: 205px; left: 66px; width: 410px;
    font-size: 7.6px; line-height: 1.42;
  }
  .salutation { margin-bottom: 12px; }
  .letter-body p.paragraph { margin-bottom: 12px; }
  .closing { margin-top: 4px; }
  .signature {
    display: block; margin: 10px 0 0 18px;
    width: 80px; height: 46px;
    background: var(--signature-tone);
    border-radius: 3px;
  }
  .contact {
    position: absolute; right: 40px; bottom: 52px;
    font-family: "Roboto", sans-serif;
    font-size: 10.5px; color: var(--ink-dark);
    text-align: left;
  }
  .contact-address { margin-bottom: 4px; padding-left: 22px; }
  .contact-line { display: flex; align-items: center; gap: 4px; white-space: nowrap; }
  .contact-item { display: inline-flex; align-items: center; gap: 3px; margin-right: 4px; }
  .contact-icon { width: 10px; height: 10px; fill: var(--icon-blue); }
</style>
</head>
<body>
<main class="canvas">
  <article class="letterhead">
    <header class="brand">
      <span class="brand-mark"></span>
      <span class="brand-name">Dunmore Hollis County Police Association</span>
    </header>

    <section class="letter-body">
      <p class="salutation">Dear customer,</p>
      <p class="paragraph">Lorem ipsum dolor sit amet, consectetur adipisicing elit, sed do eiusmod tempor incididunt ut labore et dolore magna aliqua. Ut enim ad minim veniam, quis nostrud exercitation ullamco laboris nisi ut aliquip ex ea commodo consequat. Duis aute irure dolor in reprehenderit in voluptate velit esse cillum dolore eu fugiat nulla pariatur. Excepteur sint occaecat cupidatat non proident, sunt in culpa qui officia deserunt mollit anim id est laborum.</p>
      <p class="paragraph">Lorem ipsum dolor sit amet, consectetur adipisicing elit, sed do eiusmod tempor incididunt ut labore et dolore magna aliqua. Ut enim ad minim veniam, quis nostrud exercitation ullamco laboris nisi ut aliquip ex ea commodo consequat. Duis aute irure dolor in reprehenderit in voluptate velit esse cillum dolore eu fugiat nulla pariatur. Excepteur sint occaecat cupidatat non proident, sunt in culpa qui officia deserunt mollit anim id est laborum.</p>
      <p class="paragraph">Lorem ipsum dolor sit amet, consectetur adipisicing elit, sed do eiusmod tempor incididunt ut labore et dolore magna aliqua. Ut enim ad minim veniam, quis nostrud exercitation ullamco laboris nisi ut aliquip ex ea commodo consequat. Duis aute irure dolor in reprehenderit in voluptate velit esse cillum dolore eu fugiat nulla pariatur. Excepteur sint occaecat cupidatat non proident, sunt in culpa qui officia deserunt mollit anim id est laborum.</p>
      <p class="paragraph">Lorem ipsum dolor sit amet, consectetur adipisicing elit, sed do eiusmod tempor incididunt ut labore et dolore magna aliqua. Ut enim ad minim veniam, quis nostrud exercitation ullamco laboris nisi ut aliquip ex ea commodo consequat. Duis aute irure dolor in reprehenderit.</p>
      <p class="closing">Yours Sincerely,</p>
      <span class="signature" role="img" aria-label="Handwritten signature of the sender"></span>
    </section>

    <footer class="contact">
      <p class="contact-address">48 Alder Crest Road, Dunmore, ON K7R 3P4</p>
      <p class="contact-line">
        <span class="contact-item">
          <svg class="contact-icon" viewBox="0 0 24 24" aria-hidden="true"><path d="M6.6 10.8a15.1 15.1 0 0 0 6.6 6.6l2.2-2.2c.3-.3.7-.4 1-.2 1.1.4 2.3.6 3.6.6.6 0 1 .4 1 1V20c0 .6-.4 1-1 1A17 17 0 0 1 3 4c0-.6.4-1 1-1h3.5c.6 0 1 .4 1 1 0 1.3.2 2.5.6 3.6.1.3 0 .7-.2 1z"/></svg>
          +15550142876
        </span>
        <span class="contact-item">
          <svg class="contact-icon" viewBox="0 0 24 24" aria-hidden="true"><path d="M2 5h20v14H2z M2 5l10 8 10-8" stroke="#fbfbfb" stroke-width="1.5"/></svg>
          info@dhcpa.org
        </span>
        <span class="contact-item">
          <svg class="contact-icon" viewBox="0 0 24 24" aria-hidden="true"><circle cx="12" cy="12" r="10"/><path d="M2 12h20M12 2c3 3 3 17 0 20M12 2c-3 3-3 17 0 20" stroke="#fbfbfb" stroke-width="1.5" fill="none"/></svg>
          http://www.dhcpa.org
        </span>
      </p>
    </footer>
  </article>
</main>
</body>
</html>
```